Web Design Project

Kluvora.com is an online forum for chatting with friends whilst watching TV. We have attached our wireframes, which we would like a design for. The target audience are 11-40 years old.
Please see similar sites (eg Pollent) for inspiration.
Updates

Target Market(s)

11 to 40 year olds, TV viewers

Industry/Entity Type

Tv

Requirements
Must have
• All the pages and elements included in the wireframes.
Nice to have
• Bold graphical elements.

```html
<!DOCTYPE html>
<html lang="en">
<head>
<meta charset="utf-8">
<title>Kluvora</title>
<link rel="stylesheet" href="https://fonts.googleapis.com/css2?family=Ubuntu:wght@400;500&family=Source+Sans+3:wght@400;600&display=swap">
<style>
:root{
  --ink:#1a1a1a;
  --text:#333;
  --orange:#e8441b;
  --cta:#f25a24;
  --page:#ececec;
  --panel:#f4f4f4;
  --line:#d2d2d2;
}
*{box-sizing:border-box;margin:0;padding:0}
html,body{width:750px;height:1200px;overflow:hidden}
body{position:relative;background:var(--page);font-family:"Source Sans 3",Arial,sans-serif;color:var(--text)}
.abs{position:absolute}
.topline{left:0;top:0;width:750px;height:4px;background:var(--ink)}
.header{left:0;top:4px;width:750px;height:94px;background:linear-gradient(#f6f6f6,#e9e9e9)}
.brand{left:24px;top:38px;display:flex;align-items:center;gap:8px;font-family:"Ubuntu",sans-serif;font-weight:500;font-size:30px;color:var(--ink)}
.brand .mark{width:30px;height:30px;border-radius:50%;background:var(--ink)}
.social{display:flex;gap:4px}
.social span{width:23px;height:23px;border-radius:50%;background:var(--ink);display:block}
.search{left:508px;top:60px;width:226px;height:23px;display:flex}
.search .field{flex:1;border:1px solid #c9c9c9;background:#fff;font-size:9.5px;font-style:italic;color:#666;padding:5px 9px}
.search .btn{width:55px;background:var(--ink);color:#fff;font-size:11px;display:flex;align-items:center;justify-content:center}
.nav{left:0;top:98px;width:750px;height:43px;background:linear-gradient(#eaeaea,#cfcfcf);border-top:1px solid #c8c8c8;border-bottom:1px solid #bdbdbd;display:flex}
.nav a{font-family:"Ubuntu",sans-serif;font-weight:500;font-size:11.5px;color:var(--ink);text-decoration:none;display:flex;align-items:center;justify-content:center;border-right:1px solid #b9b9b9;box-shadow:1px 0 0 #f3f3f3}
.hero{left:0;top:141px;width:750px;height:257px;background:#e3e3e3}
.slide{left:22px;top:150px;width:488px;height:231px;
  background:
    radial-gradient(ellipse 120px 150px at 18% 70%,rgba(214,170,140,.55),transparent 70%),
    radial-gradient(ellipse 110px 140px at 52% 60%,rgba(222,186,160,.5),transparent 70%),
    radial-gradient(ellipse 120px 160px at 82% 55%,rgba(230,200,176,.5),transparent 70%),
    radial-gradient(ellipse 160px 120px at 40% 10%,rgba(236,226,212,.55),transparent 70%),
    linear-gradient(180deg,#7a6150 0%,#5c4638 55%,#2f2722 100%)}
.caption{left:22px;top:350px;width:488px;height:31px;background:rgba(255,255,255,.9);display:flex;align-items:center;padding:0 10px;font-size:10.5px}
.caption b{color:var(--orange);font-weight:600}
.caption .sep{margin:0 6px;color:#555}
.caption .arrows{margin-left:auto;display:flex;gap:8px}
.card{left:516px;width:212px;height:76px;background:#fafafa;border:1px solid #d6d6d6;border-radius:2px;display:flex;gap:8px;padding:8px}
.card .thumb{width:64px;height:58px;flex:none}
.card h3{font-size:11px;font-weight:600;color:var(--orange);margin:1px 0 2px}
.card p{font-size:8.6px;line-height:1.5;color:#444}
.box{border:1px solid #cfcfcf;background:var(--panel)}
.bar{height:36px;background:linear-gradient(#2c2c2c,#0c0c0c);color:#fff;font-family:"Ubuntu",sans-serif;font-size:14px;display:flex;align-items:center;padding-left:14px}
.featured{left:18px;top:410px;width:715px;height:227px}
.prog{position:absolute;top:44px;width:166px}
.prog .poster{width:166px;height:122px}
.prog .meta{display:flex;gap:7px;margin-top:10px}
.chan{background:#2b2b2b;color:#fff;font-family:"Ubuntu",sans-serif;font-weight:500;display:flex;align-items:center;justify-content:center;flex:none}
.prog .chan{width:40px;height:35px;font-size:12px}
.prog h4{font-size:9.5px;font-weight:600;color:var(--orange)}
.prog p{font-size:9px;line-height:1.45;color:var(--ink)}
.schedule{left:19px;top:648px;width:505px;height:454px;background:#f2f2f2}
.grid{position:absolute;left:0;top:37px;width:503px}
.row{display:grid;grid-template-columns:71px 62px 70px 69px 69px 68px 84px;height:48px;border-bottom:1px solid var(--line)}
.row.head{height:23px;background:#e2e2e2}
.row.head>div{font-size:10px;font-weight:600;color:var(--ink)}
.row>div{border-right:1px solid var(--line);display:flex;align-items:center;padding-left:6px;font-size:8.6px;line-height:1.3;color:#333}
.row>div:first-child{border-right:none;padding-left:14px}
.row>div:last-child{border-right:none;padding-right:18px}
.row .chan{width:37px;height:35px;font-size:11px}
.scroll{position:absolute;left:494px;top:60px;width:6px;height:386px;background:var(--ink);border-radius:3px}
.scroll i{position:absolute;left:0;top:28px;width:6px;height:28px;background:#bbb;border-radius:3px}
.blog{left:530px;top:648px;width:204px;height:453px;background:#f2f2f2}
.blog .bhead{height:36px;background:linear-gradient(#f4f4f4,#dcdcdc);border-bottom:1px solid #cacaca;font-family:"Ubuntu",sans-serif;font-size:13.5px;color:var(--ink);display:flex;align-items:center;padding-left:11px}
.post{height:96px;border-bottom:1px solid var(--line);padding:8px 10px 0 13px}
.post h4{font-size:10px;font-weight:400;color:var(--orange);margin-bottom:3px}
.post .body{display:flex;gap:7px}
.post .pic{width:53px;height:48px;flex:none;margin-top:9px}
.post p{width:112px;font-size:8.4px;line-height:1.55;color:#333}
.post small{display:block;font-size:7.6px;color:#222;margin-top:1px}
.more{position:absolute;left:0;bottom:0;width:202px;height:20px;background:var(--cta);color:#fff;font-size:8.5px;display:flex;align-items:center;justify-content:flex-end;padding-right:20px}
.footer{left:0;top:1126px;width:750px;height:74px;background:linear-gradient(#2e2e2e,#0f0f0f)}
.footer .legal{position:absolute;left:18px;top:13px;font-size:7.5px;color:#ddd}
.footer .social{position:absolute;left:655px;top:12px}
.footer .social span{background:#f2f2f2;width:22px;height:22px}
</style>
</head>
<body>
<div class="abs topline"></div>

<header class="abs header">
  <div class="abs brand"><span class="mark"></span>Kluvora</div>
  <div class="abs social" style="left:656px;top:18px" aria-label="Social links"><span></span><span></span><span></span></div>
</header>
<div class="abs search"><div class="field">Enter Keyword</div><div class="btn">Search</div></div>

<nav class="abs nav">
  <a style="width:95px">HOME</a>
  <a style="width:98px">ABOUT US</a>
  <a style="width:146px">MY CONVERSATIONS</a>
  <a style="width:88px">SETTINGS</a>
  <a style="width:98px">CHANNELS</a>
  <a style="width:90px;border-right:none;box-shadow:none">CONTACT</a>
</nav>

<section class="abs hero"></section>
<div class="abs slide" role="img" aria-label="Promotional still of three drama cast members standing in a hallway"></div>
<div class="abs caption">
  <b>Programme/ Channel Headling goes here</b><span class="sep">|</span><span>3:00 - 4:00 PM</span>
  <span class="arrows">
    <svg width="6" height="10" viewBox="0 0 6 10"><path d="M6 0L0 5l6 5z" fill="#111"/></svg>
    <svg width="6" height="10" viewBox="0 0 6 10"><path d="M0 0l6 5-6 5z" fill="#111"/></svg>
  </span>
</div>

<article class="abs card" style="top:150px">
  <div class="thumb" role="img" aria-label="Comic hero channel artwork" style="background:radial-gradient(circle at 40% 35%,#3a78d8,transparent 60%),linear-gradient(160deg,#1e4fa8 0%,#2a66c4 45%,#d4262c 70%,#e8b22a 100%)"></div>
  <div><h3>Channel Name</h3><p>Brightlane Studios is a web service company, offering a wide range of services</p></div>
</article>
<article class="abs card" style="top:227px">
  <div class="thumb" role="img" aria-label="Action channel artwork" style="background:radial-gradient(ellipse at 50% 50%,#e0202a,transparent 65%),linear-gradient(180deg,#111 0%,#7a0d12 50%,#111 100%)"></div>
  <div><h3>Channel Name</h3><p>Brightlane Studios is a web service company, offering a wide range of services</p></div>
</article>
<article class="abs card" style="top:304px">
  <div class="thumb" role="img" aria-label="Wrestling show artwork" style="background:radial-gradient(ellipse at 50% 60%,#3aa0ff,transparent 60%),linear-gradient(180deg,#0a0f22 0%,#123a80 60%,#0a0f22 100%)"></div>
  <div><h3>Channel Name</h3><p>Brightlane Studios is a web service company, offering a wide range of services</p></div>
</article>

<section class="abs box featured">
  <div class="bar">Featured Programs</div>
  <div class="prog" style="left:11px">
    <div class="poster" role="img" aria-label="Crime drama cast poster" style="background:radial-gradient(ellipse 90px 60px at 50% 20%,rgba(190,180,150,.55),transparent 70%),linear-gradient(180deg,#6b6656 0%,#3b3830 60%,#1f1d19 100%)"></div>
    <div class="meta"><span class="chan">Vela</span><div><h4>Program Name here</h4><p>2:00 am to 3:00 am<br>learn more</p></div></div>
  </div>
  <div class="prog" style="left:187px">
    <div class="poster" role="img" aria-label="Comedy series still in a living room" style="background:radial-gradient(ellipse 70px 60px at 30% 45%,rgba(200,160,110,.55),transparent 70%),radial-gradient(ellipse 50px 50px at 72% 30%,rgba(170,150,120,.5),transparent 70%),linear-gradient(180deg,#716a52 0%,#433c2c 60%,#2a241a 100%)"></div>
    <div class="meta"><span class="chan">Orbit</span><div><h4>Program Name here</h4><p>2:00 am to 3:00 am<br>learn more</p></div></div>
  </div>
  <div class="prog" style="left:362px">
    <div class="poster" role="img" aria-label="Prison drama poster behind chain-link fence" style="background:radial-gradient(ellipse 80px 70px at 65% 45%,rgba(240,190,120,.6),transparent 70%),linear-gradient(135deg,#d49a48 0%,#a86e2c 50%,#4a3018 100%)"></div>
    <div class="meta"><span class="chan">Quad</span><div><h4>Program Name here</h4><p>2:00 am to 3:00 am<br>learn more</p></div></div>
  </div>
  <div class="prog" style="left:538px">
    <div class="poster" role="img" aria-label="Sitcom cast poster" style="background:radial-gradient(ellipse 60px 50px at 48% 40%,rgba(230,200,170,.6),transparent 70%),linear-gradient(180deg,#b8c4c6 0%,#5a6468 45%,#1c2024 75%,#8a1c24 100%)"></div>
    <div class="meta"><span class="chan">Vela</span><div><h4>Program Name here</h4><p>2:00 am to 3:00 am<br>learn more</p></div></div>
  </div>
</section>

<section class="abs box schedule">
  <div class="bar">Program Schedule</div>
  <div class="grid">
    <div class="row head"><div>Channel</div><div>9:00</div><div>9:30</div><div>10:00</div><div>10:30</div><div>11:00</div><div>12:00</div></div>
    <div class="row"><div><span class="chan">Orbit</span></div><div>Program Name goes here</div><div>Program Name goes here</div><div>Program Name goes here</div><div>Program Name goes here</div><div>Program Name goes here</div><div>Program Name goes here</div></div>
    <div class="row"><div><span class="chan">Ember</span></div><div>Program Name goes here</div><div>Program Name goes here</div><div>Program Name goes here</div><div>Program Name goes here</div><div>Program Name goes here</div><div>Program Name goes here</div></div>
    <div class="row"><div><span class="chan">Trio</span></div><div>Program Name goes here</div><div>Program Name goes here</div><div>Program Name goes here</div><div>Program Name goes here</div><div>Program Name goes here</div><div>Program Name goes here</div></div>
    <div class="row"><div><span class="chan">Quad</span></div><div>Program Name goes here</div><div>Program Name goes here</div><div>Program Name goes here</div><div>Program Name goes here</div><div>Program Name goes here</div><div>Program Name goes here</div></div>
    <div class="row"><div><span class="chan">Vela</span></div><div>Program Name goes here</div><div>Program Name goes here</div><div>Program Name goes here</div><div>Program Name goes here</div><div>Program Name goes here</div><div>Program Name goes here</div></div>
    <div class="row"><div><span class="chan">Warp</span></div><div>Program Name goes here</div><div>Program Name goes here</div><div>Program Name goes here</div><div>Program Name goes here</div><div>Program Name goes here</div><div>Program Name goes here</div></div>
    <div class="row"><div><span class="chan">Tidal</span></div><div>Program Name goes here</div><div>Program Name goes here</div><div>Program Name goes here</div><div>Program Name goes here</div><div>Program Name goes here</div><div>Program Name goes here</div></div>
    <div class="row" style="border-bottom:none"><div><span class="chan">Zed</span></div><div>Program Name goes here</div><div>Program Name goes here</div><div>Program Name goes here</div><div>Program Name goes here</div><div>Program Name goes here</div><div>Program Name goes here</div></div>
  </div>
  <div class="scroll"><i></i></div>
</section>

<aside class="abs box blog">
  <div class="bhead">Recent Blog Post</div>
  <div class="post"><h4>Show or headline here</h4><div class="body"><div class="pic" role="img" aria-label="Portrait photo for blog post" style="background:radial-gradient(ellipse 20px 24px at 55% 45%,#d8a888,transparent 75%),linear-gradient(90deg,#3a2418,#8a5a40 60%,#e8e0d8)"></div><div><p>There's an article on City news about that Northbeat lad deleting his account. RIP Journalism.</p><small>learn more &nbsp;| &nbsp;8 hours ago</small></div></div></div>
  <div class="post"><h4>Show or headline here</h4><div class="body"><div class="pic" role="img" aria-label="Portrait photo for blog post" style="background:radial-gradient(ellipse 20px 24px at 50% 55%,#b88a68,transparent 75%),linear-gradient(180deg,#6a7040,#3a2a1e)"></div><div><p>There's an article on City news about that Northbeat lad deleting his account. RIP Journalism.</p><small>learn more &nbsp;| &nbsp;8 hours ago</small></div></div></div>
  <div class="post"><h4>Show or headline here</h4><div class="body"><div class="pic" role="img" aria-label="Portrait photo for blog post" style="background:radial-gradient(ellipse 20px 24px at 50% 55%,#d0a084,transparent 75%),linear-gradient(180deg,#d8dce0,#2a2420)"></div><div><p>There's an article on City news about that Northbeat lad deleting his account. RIP Journalism.</p><small>learn more &nbsp;| &nbsp;8 hours ago</small></div></div></div>
  <div class="post" style="border-bottom:none"><h4>Show or headline here</h4><div class="body"><div class="pic" role="img" aria-label="Photo of two people for blog post" style="background:radial-gradient(ellipse 14px 22px at 30% 45%,#e0b888,transparent 75%),radial-gradient(ellipse 14px 22px at 70% 45%,#c89870,transparent 75%),linear-gradient(90deg,#a88458,#6a5038)"></div><div><p>There's an article on City news about that Northbeat lad deleting his account. RIP Journalism.</p><small>learn more &nbsp;| &nbsp;8 hours ago</small></div></div></div>
  <div class="more">View more blog</div>
</aside>

<footer class="abs footer">
  <div class="legal">© 2012 Company Name &nbsp;| &nbsp;All right resreved &nbsp;| &nbsp;Term &amp; Conditions</div>
  <div class="social" aria-label="Social links"><span></span><span></span><span></span></div>
</footer>
</body>
</html>
```